依頼詳細
■入れてほしい文言
エクセルデータ参照してください

■ のぼり、ポスターサイズ情報
サイズ:横600mm×縦1800mm以内

■ デザインへの要望
洋風調、和風調 のぼりデザインを作成したい
デザイン参考に添付ファイルの画像を参照
記載項目
サイズ:横600mm×縦1800mm以内
希望イメージ
シンプル 複雑
単色 カラフル
暗い 明るい
日常 高級
遊び心 厳粛
未来的 伝統的
女性的 男性的
希望する色
納品ファイル
• イラストレーター形式 (.ai)
• フォトショップ形式 (.psd)
• PNG形式 (.png)
補足説明

```html
<!DOCTYPE html>
<html lang="ja">
<head>
<meta charset="utf-8">
<title>越後の小京都 のぼり</title>
<link href="https://fonts.googleapis.com/css2?family=Yuji+Syuku&family=Noto+Serif+JP:wght@900&display=swap" rel="stylesheet">
<style>
  :root {
    --navy: #1b2070;
    --navy-deep: #151a5c;
    --white: #ffffff;
    --wood-dark: #6b3c22;
    --wood-mid: #a8673f;
    --wood-light: #d9a57c;
    --paper: #f3ece4;
  }
  html, body {
    margin: 0;
    padding: 0;
    width: 1200px;
    height: 3628px;
    overflow: hidden;
    background: var(--white);
  }
  .banner {
    position: relative;
    width: 1200px;
    height: 3628px;
    overflow: hidden;
  }
  .photo {
    position: absolute;
    left: 0;
    width: 1200px;
  }
  .photo-craftsman {
    top: 0;
    height: 1040px;
    background: linear-gradient(180deg, #5a3a2a 0%, #8a5a3c 35%, #b07a52 70%, #9a5f3a 100%);
  }
  .photo-slats {
    top: 1040px;
    height: 200px;
    background: linear-gradient(180deg, #8d4e2c 0%, var(--wood-mid) 60%, #7a4326 100%);
  }
  .photo-lattice {
    top: 1240px;
    height: 1520px;
    background: radial-gradient(ellipse at 50% 45%, var(--paper) 0%, #e6d3c2 45%, #c99a78 100%);
  }
  .photo-lower-slats {
    top: 2760px;
    height: 580px;
    background: linear-gradient(180deg, var(--wood-mid) 0%, #8d4e2c 40%, var(--wood-dark) 100%);
  }
  .title-panel {
    position: absolute;
    left: 428px;
    top: 732px;
    width: 392px;
    height: 2068px;
    background: var(--navy);
    box-sizing: border-box;
  }
  .title-panel::before {
    content: "";
    position: absolute;
    inset: 18px;
    border: 5px solid var(--white);
  }
  .title-text {
    position: absolute;
    left: 0;
    right: 0;
    top: 90px;
    margin: 0 auto;
    writing-mode: vertical-rl;
    font-family: "Yuji Syuku", serif;
    font-weight: 400;
    color: var(--white);
    font-size: 270px;
    line-height: 1;
    letter-spacing: 20px;
    width: 280px;
    text-align: start;
  }
  .title-text .small {
    font-size: 190px;
    display: inline-block;
    margin: 10px 0 30px;
  }
  .footer-band {
    position: absolute;
    left: 0;
    top: 3340px;
    width: 1200px;
    height: 288px;
    background: var(--navy-deep);
    border-top: 6px solid var(--white);
    box-sizing: border-box;
    display: flex;
    align-items: center;
    justify-content: center;
  }
  .org-name {
    font-family: "Noto Serif JP", serif;
    font-weight: 900;
    font-size: 148px;
    color: var(--white);
    letter-spacing: 2px;
    margin: 0;
    line-height: 1;
  }
</style>
</head>
<body>
  <div class="banner">
    <div class="photo photo-craftsman" role="img" aria-label="職人の手がかんなで木材を削る作業場の写真"></div>
    <div class="photo photo-slats" role="img" aria-label="木製の格子桟の写真"></div>
    <div class="photo photo-lattice" role="img" aria-label="麻の葉模様の組子障子の写真"></div>
    <div class="photo photo-lower-slats" role="img" aria-label="木製の縦格子の写真"></div>

    <div class="title-panel">
      <h1 class="title-text">越後<span class="small">の</span>小京都</h1>
    </div>

    <div class="footer-band">
      <p class="org-name">青嶺建具組合</p>
    </div>
  </div>
</body>
</html>
```